Heronby Mortgage Capital Business Card

We need a business card design for our mortgage servicing company. In addition to servicing the loans of homeowners, we help homeowners with purchasing their homes and any mortgage refinancing. We would like to see designs that use the colors in the logo attached below (gold-ish yellow and navy blue), and any other design you deem fit! The design should communicate a simpler life with smart mortgages provided by Heronby.

```html
<!DOCTYPE html>
<html lang="en">
<head>
<meta charset="utf-8">
<title>Heronby Mortgage Capital – Business Card</title>
<link href="https://fonts.googleapis.com/css2?family=Arimo:wght@400;700&display=swap" rel="stylesheet">
<style>
  :root {
    --gold: #e0b040;
    --navy: #1f1d5c;
    --ink: #3d3d3d;
    --muted: #808080;
    --rule: #cfcfcf;
    --paper: #ffffff;
    --stage: #e9e9ec;
  }
  * { box-sizing: border-box; margin: 0; padding: 0; }
  html, body { width: 1200px; height: 874px; overflow: hidden; }
  body {
    background: var(--stage);
    font-family: "Arimo", Arial, sans-serif;
    position: relative;
  }
  .card {
    position: absolute;
    left: 330px;
    width: 540px;
    height: 309px;
    border-radius: 18px;
    overflow: hidden;
    box-shadow: 0 6px 18px rgba(0,0,0,0.18);
  }
  /* Back side */
  .card-back { top: 98px; background: var(--gold); }
  .card-back .wordmark {
    position: absolute; left: 0; right: 0; top: 100px;
    display: flex; align-items: center; justify-content: center; gap: 14px;
    color: var(--navy); font-weight: 700; font-size: 50px;
  }
  .wordmark .mark-dot {
    width: 18px; height: 18px; border-radius: 50%; background: currentColor;
  }
  .card-back .tagline {
    position: absolute; left: 0; right: 0; top: 228px;
    text-align: center; color: var(--navy); font-size: 15px;
  }
  /* Front side */
  .card-front { top: 467px; background: var(--paper); }
  .card-front .wordmark {
    position: absolute; right: 60px; top: 58px;
    display: flex; align-items: center; gap: 10px;
    color: var(--navy); font-weight: 700; font-size: 36px;
  }
  .card-front .wordmark .mark-dot { width: 13px; height: 13px; background: var(--gold); }
  .person { position: absolute; left: 40px; top: 118px; }
  .person .name { color: var(--navy); font-weight: 700; font-size: 25px; }
  .person .role { color: var(--muted); font-size: 13px; margin-top: 2px; }
  .divider {
    position: absolute; left: 40px; right: 40px; top: 176px;
    border-top: 1px solid var(--rule);
  }
  .contacts { position: absolute; left: 40px; top: 188px; list-style: none; }
  .contacts li {
    display: flex; align-items: center; gap: 8px;
    color: var(--ink); font-size: 14px; line-height: 19px;
  }
  .contacts svg { width: 12px; height: 12px; fill: var(--gold); flex: none; }
  .address {
    position: absolute; right: 40px; top: 192px;
    text-align: right; color: var(--ink); font-size: 14px; line-height: 19px;
  }
  .band-gold { position: absolute; left: 0; right: 0; bottom: 20px; height: 3px; background: var(--gold); }
  .band-navy { position: absolute; left: 0; right: 0; bottom: 0; height: 17px; background: var(--navy); }
</style>
</head>
<body>
  <section class="card card-back" aria-label="Card back">
    <div class="wordmark"><span class="mark-dot"></span>Heronby Mortgage</div>
    <p class="tagline">Simpler life with smart mortgages</p>
  </section>

  <section class="card card-front" aria-label="Card front">
    <div class="wordmark"><span class="mark-dot"></span>Heronby Mortgage</div>
    <div class="person">
      <p class="name">Daniel Ward</p>
      <p class="role">President</p>
    </div>
    <div class="divider"></div>
    <ul class="contacts">
      <li><svg viewBox="0 0 24 24" aria-hidden="true"><path d="M6.6 10.8a15.1 15.1 0 0 0 6.6 6.6l2.2-2.2a1 1 0 0 1 1-.25 11.4 11.4 0 0 0 3.6.57 1 1 0 0 1 1 1V20a1 1 0 0 1-1 1A17 17 0 0 1 3 4a1 1 0 0 1 1-1h3.5a1 1 0 0 1 1 1 11.4 11.4 0 0 0 .57 3.6 1 1 0 0 1-.25 1z"/></svg>555-210-4187</li>
      <li><svg viewBox="0 0 24 24" aria-hidden="true"><path d="M7 1h10a2 2 0 0 1 2 2v18a2 2 0 0 1-2 2H7a2 2 0 0 1-2-2V3a2 2 0 0 1 2-2zm0 3v14h10V4z"/></svg>555-210-9362</li>
      <li><svg viewBox="0 0 24 24" aria-hidden="true"><path d="M2 5h20v14H2zm2 2v.5l8 5 8-5V7l-8 5z"/></svg>info@heronbymortgage.com</li>
    </ul>
    <div class="address">
      <p>412 Alder Court</p>
      <p>Fairview, Canada 20418</p>
      <p>www.heronbymortgage.com</p>
    </div>
    <div class="band-gold"></div>
    <div class="band-navy"></div>
  </section>
</body>
</html>
```